K.O.V Ventures - Business Card

We need a business card design for a new company based in Malaysia, called K.O.V Ventures Sdn. Bhd. We create, develop & customize database & software/web-based business systems to suit our clients need, mainly in oil&gas industry.

We would like to challenge the creativity of you to design a simple, meaningful, modern, professional & sleek. The design concept may varies but worthy enough for the recipients to proudly keep it in their wallet, and award us with fruitful business opportunities.

B-7-12 Lantera Plaza,
PJU9/4, Damai Perdana,
48300 Perak. Malaysia

http://kovventures-example.com

HAFIZ Rosman | +6000-5550123 | Co-Founder
Di Kamarul | +6012-4190273 | Co-Founder
Amir Syukri | +6019-3306158 | Managing Director

Target Market(s)

The target market will expand to several other industries such as aviation, communication, automotive, education & hotel.

Industry/Entity Type

Business

Font styles to use
Serif
Sans Serif
Decorative
Script

Requirements
Must have
• plain background yet colourful concept.
Should not have
• something too easy that I can draw myself

```html
<!DOCTYPE html>
<html lang="en">
<head>
<meta charset="utf-8">
<title>K.O.V Ventures - Business Card</title>
<link rel="stylesheet" href="https://fonts.googleapis.com/css2?family=PT+Serif:wght@400;700&family=Roboto+Condensed:wght@400;500&display=swap">
<style>
  :root {
    --page: #e9e6e1;
    --card: #050505;
    --card-top: #1a1a1a;
    --blue: #0e6aa6;
    --pink: #ec0a6e;
    --green: #46a80c;
    --white: #ffffff;
    --orange: #f07c12;
    --teal: #12a5a0;
    --violet: #7a2bc4;
    --lime: #b6d80f;
    --sky: #2aa8e6;
  }
  html, body {
    margin: 0;
    width: 1200px;
    height: 1200px;
    overflow: hidden;
    background: var(--page);
  }
  .card {
    position: absolute;
    left: 320px;
    top: 110px;
    width: 560px;
    height: 980px;
    overflow: hidden;
    background: linear-gradient(180deg, var(--card-top) 0%, var(--card) 45%, var(--card) 100%);
    box-shadow: 0 10px 30px rgba(0,0,0,0.25);
  }
  .brand {
    position: absolute;
    left: 130px;
    top: 110px;
    width: 300px;
    height: 240px;
    border-radius: 50%;
    background: radial-gradient(circle, rgba(255,255,255,0.08) 0%, rgba(255,255,255,0.03) 45%, rgba(0,0,0,0) 70%);
    display: flex;
    flex-direction: column;
    align-items: center;
    justify-content: center;
    gap: 14px;
  }
  .brand-dot {
    width: 46px;
    height: 46px;
    border-radius: 50%;
    background: var(--pink);
  }
  .brand-name {
    font-family: "Roboto Condensed", sans-serif;
    font-weight: 500;
    font-size: 26px;
    letter-spacing: 1px;
    color: var(--white);
  }
  .name-tag {
    position: absolute;
    left: -40px;
    top: 480px;
    width: 380px;
    height: 96px;
    border-radius: 48px;
    background: var(--blue);
    z-index: 2;
    font-family: "PT Serif", serif;
    color: var(--white);
  }
  .name-tag .person {
    position: absolute;
    left: 70px;
    top: 10px;
    font-size: 36px;
    white-space: nowrap;
  }
  .name-tag .role {
    position: absolute;
    left: 150px;
    top: 54px;
    font-size: 25px;
    white-space: nowrap;
  }
  .band {
    position: absolute;
    left: 0;
    width: 100%;
    display: flex;
    align-items: center;
    font-family: "Roboto Condensed", sans-serif;
    color: var(--white);
  }
  .address-band {
    top: 560px;
    height: 140px;
    background: var(--pink);
    padding-top: 30px;
    box-sizing: border-box;
  }
  .address-band .icon { margin: 0 16px 0 40px; flex: none; }
  .address-band p {
    margin: 0;
    font-size: 25px;
    font-weight: 500;
    line-height: 1.25;
  }
  .phone-band {
    top: 745px;
    height: 120px;
    background: var(--green);
  }
  .phone-band .icon { margin: 0 20px 0 40px; flex: none; }
  .phone-band .number {
    font-size: 42px;
    font-weight: 500;
  }
  .color-stripe {
    position: absolute;
    left: 0;
    bottom: 0;
    width: 100%;
    height: 22px;
    display: flex;
  }
  .color-stripe span { flex: 1; }
  .s-orange { background: var(--orange); }
  .s-teal { background: var(--teal); }
  .s-violet { background: var(--violet); }
  .s-lime { background: var(--lime); }
  .s-sky { background: var(--sky); }
  .s-pink { background: var(--pink); }
</style>
</head>
<body>
  <div class="card">
    <div class="brand">
      <div class="brand-dot"></div>
      <div class="brand-name">K.O.V Ventures</div>
    </div>

    <div class="name-tag">
      <span class="person">Hafiz Rosman</span>
      <span class="role">Co-Founder</span>
    </div>

    <div class="band address-band">
      <svg class="icon" width="34" height="34" viewBox="0 0 34 34" aria-hidden="true">
        <circle cx="17" cy="17" r="16" fill="#ffffff"/>
        <path d="M8 17 L17 9 L26 17 L23 17 L23 25 L19 25 L19 20 L15 20 L15 25 L11 25 L11 17 Z" fill="#ec0a6e"/>
      </svg>
      <p>B-7-12 Lantera Plaza, PJU9/4,<br>Damai Perdana, 48300 Perak. Malaysia</p>
    </div>

    <div class="band phone-band">
      <svg class="icon" width="44" height="44" viewBox="0 0 44 44" aria-hidden="true">
        <circle cx="22" cy="22" r="19" fill="none" stroke="#ffffff" stroke-width="3"/>
        <path d="M15 13 C13 15 13 19 16 24 C19 29 24 32 28 32 C30 32 31 30 31 29 L27 26 L25 28 C22 27 18 23 17 20 L19 18 L17 13 Z" fill="#ffffff"/>
      </svg>
      <span class="number">+6000-5550123</span>
    </div>

    <div class="color-stripe">
      <span class="s-teal"></span>
      <span class="s-orange"></span>
      <span class="s-violet"></span>
      <span class="s-lime"></span>
      <span class="s-sky"></span>
      <span class="s-pink"></span>
    </div>
  </div>
</body>
</html>
```